Flyer für Pelz- & Schmuck-Ausstellung
Zielgruppe
Wir haben Pelz & Schmuck Ausstellungen in Wien.
Unsere Zielgruppe sind ältere Leute aus Wien.
Wir kaufen auch andere Sachen wie Goldschmuck Crocotaschen & Ledermäntel.
Aufgabenstellung
Unser Flyer hätte 2 Seiten.
Dina 4
Wir würden uns freuen wenn ich schon bis Dienstag die Designs zum entscheiden hätten.
Die 1 Seite von unserem Flyer schicke ich als Upload.
Es müssten Kleinigkeiten wie Hintergrund Farben und kleine Texte geändert werden.
Für bessere aufwertendere Vorschläge würden wir uns natürlich freuen.
Das Bild von der älteren Dame würden wir rausmachen & tauschen mit dem Bild von der Designerin. (Unten in uploads)
Uns gefällt der Hintergrund von der Jungdesignerin nicht.
Vlt könnten sie die Jungdesignerin und den Pelz in einer besseren location einfügen. So das es harmonisch und auch nicht groß gefaked aussieht.
Statt Aktion im kerno.
Aktion im 19 Bezirk
Den unteren rechteckigen Kasten bitte in der gleichen Farbe wie der Hut von der Dame wäre.
Und Aktion auch in dieser Farbe.
Den Kasten können sie dort hinmachen wo er optisch am besten hinpasst.
Aktion 5 Tage gültig!
Kalender bleiben
Der untere Text wird geändert.
Dann haben sie unten
Modehaus Selvig: kostenloser Senioren-Besuchsdienst
Terminvergabe nach Telefonischer Absprache unter 0664 392617
Dringend gesucht für Pelz & Schmuck Austellungen in der 1010 Wendelgasse 4b.
Bitte den Text unten etwas größer deutlicher Als es zuvor war.
Wenn sie das Bild etwas kleiner machen würden wäre hätte man sicher unten etwas mehr Platz .
Dann wäre noch die Rückseite.
Hier können sie ihren Ideen und Design Vorschläge freien Lauf lassen.
In der Rückseite soll es sich darum Handeln das wir auch für unsere Ausstellungen verschiedene Sachen kaufen.
Ankauf von Mode & Schmuck für Ausstellungen von Modehaus Selvig
Ledermäntel
Vlt. so ähnlich was das Bild was ich reingeschickt habe.
Jetzt neu! Ankauf von Leder Jacken aller Art…
Pelzmäntel alle..

```html
<!DOCTYPE html>
<html lang="de">
<head>
<meta charset="utf-8">
<title>Flyer Pelz &amp; Schmuck Ausstellung</title>
<link href="https://fonts.googleapis.com/css2?family=Montserrat:wght@300;400;500;600;700;800;900&display=swap" rel="stylesheet">
<style>
:root{
  --stage:#5f5f5f;
  --brown-dark:#6b4a1f;
  --brown:#7f5a26;
  --gold-deep:#a88a45;
  --gold:#c7a75a;
  --gold-light:#e9d08c;
  --gold-pale:#f3e3b4;
  --ink-brown:#6a4618;
  --text:#222;
  --white:#fff;
}
*{margin:0;padding:0;box-sizing:border-box}
html,body{width:1200px;height:1117px;overflow:hidden;background:var(--stage);font-family:"Montserrat",sans-serif}
.page{position:absolute;top:177px;width:541px;height:763px;overflow:hidden}
.page--front{left:55px;background:var(--gold)}
.page--back{left:617px;background:var(--white)}
.abs{position:absolute}
.center{left:0;right:0;text-align:center}
svg.layer{position:absolute;left:0;top:0}

/* front */
.front-top{left:0;top:0;width:541px;height:240px;background:linear-gradient(180deg,var(--brown) 0%,var(--brown-dark) 100%)}
.front-kicker{top:28px;font-size:19px;font-weight:400;color:var(--white);letter-spacing:.3px}
.front-kicker b{font-weight:700;color:var(--gold-light)}
.front-title{top:60px;font-weight:900;color:var(--white);line-height:46px}
.front-title .l1{font-size:44px;display:block;letter-spacing:.5px}
.front-title .l2{font-size:42px;display:block;font-weight:800}
.front-title .l3{font-size:44px;display:block;font-weight:800;color:var(--gold-light)}
.front-photo{left:0;top:270px;width:541px;height:370px;background:linear-gradient(135deg,#f2ede8 0%,#e8d9cb 45%,#b8855a 70%,#3d4a3a 100%)}
.front-tab{left:0;top:225px;width:284px;height:48px;border-radius:0 12px 12px 0;background:linear-gradient(90deg,var(--gold-light),var(--gold-pale));padding:8px 0 0 44px;font-size:12px;font-weight:700;color:var(--ink-brown);line-height:16px}
.front-foot-title{top:672px;font-size:15px;font-weight:800;color:var(--white);letter-spacing:.2px}
.front-foot-text{top:697px;font-size:12.5px;font-weight:700;color:var(--white);line-height:16px}

/* back */
.back-top{left:0;top:0;width:541px;height:250px;background:linear-gradient(135deg,#c9a85a 0%,#dcc27b 50%,#c4a356 100%)}
.back-head{left:0;width:340px;text-align:center;color:var(--white)}
.back-aktion{top:28px;font-size:42px;font-weight:800;letter-spacing:1px}
.back-days{top:70px;font-size:62px;font-weight:900;line-height:66px}
.back-valid{top:130px;font-size:40px;font-weight:300;letter-spacing:2px}
.back-calendar{top:177px;font-size:20px;font-weight:700}
.item-photo{border-radius:6px}
.photo-fur{left:290px;top:20px;width:226px;height:372px;background:linear-gradient(160deg,#efe6dc 0%,#b89a80 40%,#e9ddd0 100%)}
.photo-leather{left:312px;top:186px;width:212px;height:290px;background:linear-gradient(160deg,#9c4830 0%,#7b3322 60%,#5e2418 100%)}
.back-heading{left:42px;top:273px;font-size:17px;font-weight:800;color:var(--ink-brown);line-height:19.5px}
.back-lead{left:42px;top:365px;font-size:10px;font-weight:700;color:var(--gold-deep);line-height:12.5px}
.back-body{left:42px;top:413px;width:232px;font-size:10px;color:var(--text);line-height:12.5px}
.back-body p{margin-bottom:12px}
.badge{left:296px;top:461px;width:202px;height:202px;border-radius:50%;background:radial-gradient(circle at 40% 35%,#e6cc85,#b8953f 70%);border:5px solid var(--gold-pale);text-align:center;color:var(--white);padding-top:62px}
.badge-title{font-size:24px;font-weight:800}
.badge-text{font-size:17px;font-weight:400;line-height:20px}
.back-foot{left:0;top:640px;width:541px;height:123px;background:linear-gradient(180deg,var(--brown) 0%,var(--brown-dark) 100%)}
.back-foot-title{top:682px;font-size:20px;font-weight:800;color:var(--gold-light);letter-spacing:.5px}
.back-foot-text{top:710px;font-size:11.5px;font-weight:700;color:var(--white);line-height:16px}
</style>
</head>
<body>

<section class="page page--front">
  <div class="abs front-top"></div>
  <div class="abs front-photo" role="img" aria-label="Jungdesignerin in einem hellen Modeatelier neben einer Schneiderpuppe mit Pelzkragen"></div>
  <svg class="layer" width="541" height="763" viewBox="0 0 541 763" aria-hidden="true">
    <defs>
      <linearGradient id="frontGold" x1="0" x2="1"><stop offset="0" stop-color="#b8974c"/><stop offset=".5" stop-color="#d7bb6e"/><stop offset="1" stop-color="#b3924a"/></linearGradient>
    </defs>
    <path d="M0 240 L0 272 L541 272 L541 208 C430 203 360 250 280 272 Z" fill="#ffffff"/>
    <path d="M280 270 C360 248 440 203 541 208" stroke="#e9d08c" stroke-width="5" fill="none"/>
    <path d="M0 632 C120 645 230 615 330 595 C420 578 490 575 541 578 L541 763 L0 763 Z" fill="url(#frontGold)"/>
    <path d="M0 627 C120 640 230 610 330 590 C420 573 490 570 541 573" stroke="#f3e3b4" stroke-width="4" fill="none"/>
    <path d="M0 652 C150 665 260 635 360 618 C440 605 500 612 541 620" stroke="#8a6a2e" stroke-width="2" fill="none" opacity=".6"/>
  </svg>
  <div class="abs front-tab">Ankauf von Pelzen &amp; Taschen aller<br>Art In Verbindung mit Gold!</div>
  <div class="abs center front-kicker">AKTION <b>IM 19 BEZIRK</b></div>
  <h1 class="abs center front-title"><span class="l1">JUNGDESIGNER</span><span class="l2">kauft Pelzmantel</span><span class="l3">bis zu 5000!</span></h1>
  <div class="abs center front-foot-title">KOSTENLOSER SENIOREN-BESUCHSDIENST</div>
  <div class="abs center front-foot-text">Terminvergabe nach Telefonischer Absprache unter 0664 392617<br>Dringend gesucht für Pelz &amp; Schmuck Austellungen<br>in der 1010 Wendelgasse 4b.</div>
</section>

<section class="page page--back">
  <div class="abs back-top"></div>
  <svg class="layer" width="541" height="763" viewBox="0 0 541 763" aria-hidden="true">
    <path d="M0 250 C120 210 250 215 360 240 C430 255 490 250 541 240 L541 260 L0 260 Z" fill="#ffffff"/>
    <path d="M0 245 C120 205 250 210 360 235 C430 250 490 245 541 235" stroke="#f3e3b4" stroke-width="5" fill="none"/>
    <path d="M0 600 C110 650 230 650 330 625 C420 600 490 590 541 600 L541 650 L0 650 Z" fill="#c7a75a"/>
    <path d="M0 595 C110 645 230 645 330 620 C420 595 490 585 541 595" stroke="#e9d08c" stroke-width="4" fill="none"/>
  </svg>
  <div class="abs item-photo photo-fur" role="img" aria-label="Heller Pelzmantel mit Fuchskragen auf einer Büste"></div>
  <div class="abs item-photo photo-leather" role="img" aria-label="Rotbraune Lederjacke mit Reißverschlüssen"></div>
  <div class="abs back-head back-aktion">AKTION</div>
  <div class="abs back-head back-days">5 TAGE</div>
  <div class="abs back-head back-valid">GÜLTIG!</div>
  <div class="abs back-head back-calendar">Kalender bleiben</div>
  <h2 class="abs back-heading">ANKAUF VON MODE<br>AND SCHMUCK FÜR<br>AUSSTELLUNGEN<br>VON MODEHAUS SELVIG</h2>
  <div class="abs back-lead">Pelzmäntel aller Art. Mit Bild von Pelz<br>Ankauf von Pelzen aller Art Bis zu 5000 Euro<br>für hochwertige Stücke</div>
  <div class="abs back-body">
    <p>Crocotaschen gesucht. Mit Bild Zur weiter Verarbeitung von hochwertigen Gürtel.</p>
    <p>Wir zahlen für Goldschmuck bis zu<br>60 Euro das Gramm.</p>
    <p>Jungdesigner Arbeiten &amp; Designen alten Goldschmuck um.<br>Der umgearbeitete Schmuck wird zertifiziert und dann auf unseren Pelz &amp; Schmuckaustellung in Wien zu Super Preisen verkauft.</p>
    <p>Ein vorher nachher Bild von alten<br>Schmuck der umgearbeitet wurden ist.</p>
  </div>
  <div class="abs badge"><div class="badge-title">Jetzt neu!</div><div class="badge-text">Ankauf von Leder<br>Jacken aller Art...</div></div>
  <div class="abs back-foot"></div>
  <div class="abs center back-foot-title">SIE HÄTTEN ETWAS ZUM VERKAUF?</div>
  <div class="abs center back-foot-text">Dann Setzen sie sich jetzt mit einer unserer Designerinnen in Verbindung.<br>bitte Modehaus Selvig Wendelgasse 4, 1010 Wien</div>
</section>

</body>
</html>
```